Marlow Hire Business Card for recruitment company

We are looking for a Business Card Design that incorporates our personal details and our busines name and logo. We are a specialized search consultancy that recruit Property and Construction professionals.
We would like a business card that stands out and is appealing to the Construction and Property industry as well.

Target Market(s)

people in the construction and property industry

Contact Information for Business Card

Business Name and logo

Font styles to use
Serif

Colors
0094D4
00A9DD
6FCCEA
C7EBF8
E9F6FB

Requirements
Must have
• Business name and logo as well as contact details
Should not have
• No photos of us please

```html
<!DOCTYPE html>
<html lang="en">
<head>
<meta charset="utf-8">
<title>Marlow Hire Business Card</title>
<link href="https://fonts.googleapis.com/css2?family=Montserrat:wght@300;400;500;700&display=swap" rel="stylesheet">
<style>
  :root {
    --navy: #033d52;
    --teal: #00536e;
    --mist: #8fa9b5;
    --paper: #ffffff;
    --ink: #1c2226;
    --backdrop: #f2f2f2;
  }
  * { margin: 0; padding: 0; box-sizing: border-box; }
  html, body {
    width: 800px; height: 1200px; overflow: hidden;
    background: var(--backdrop);
    font-family: "Montserrat", sans-serif;
  }
  .sheet {
    position: relative; width: 800px; height: 1200px;
    display: flex; justify-content: center; align-items: center; gap: 40px;
  }
  .card {
    position: relative; width: 340px; height: 595px; overflow: hidden;
    box-shadow: 0 10px 30px rgba(0,0,0,0.18);
  }
  .card-front { background: var(--navy); }
  .card-back { background: var(--paper); }
  .front-panels {
    position: absolute; inset: 0;
    background: linear-gradient(90deg, var(--teal) 0%, var(--navy) 28%, var(--navy) 72%, var(--teal) 100%);
  }
  .back-header {
    position: absolute; top: 0; left: 0; right: 0; height: 210px;
    background: linear-gradient(180deg, var(--navy) 0%, var(--navy) 70%, var(--teal) 100%);
  }
  .brand-name {
    position: absolute; left: 0; right: 0; text-align: center;
    color: var(--paper); font-weight: 300; font-size: 36px;
    letter-spacing: 0.5px; text-transform: uppercase; line-height: 44px;
  }
  .card-front .brand-name { top: 257px; }
  .card-back .brand-name { top: 67px; }
  .front-web {
    position: absolute; top: 510px; left: 0; right: 0; text-align: center;
    color: var(--paper); font-weight: 700; font-size: 14px; letter-spacing: 3.5px;
  }
  .bottom-bar {
    position: absolute; bottom: 0; left: 45px; width: 250px; height: 5px;
    border-radius: 4px 4px 0 0;
  }
  .card-front .bottom-bar { background: var(--mist); }
  .card-back .bottom-bar { background: var(--navy); }
  .person { position: absolute; top: 248px; left: 0; right: 0; text-align: center; }
  .person-name { color: var(--navy); font-weight: 700; font-size: 26px; letter-spacing: 1px; line-height: 32px; }
  .person-role { color: var(--ink); font-weight: 400; font-size: 13px; letter-spacing: 0.4px; }
  .hours { position: absolute; top: 322px; left: 0; right: 0; text-align: center; line-height: 20px; }
  .hours-days { color: var(--navy); font-weight: 700; font-size: 16px; }
  .hours-time { color: var(--ink); font-weight: 500; font-size: 16px; letter-spacing: 0.3px; }
  .divider {
    position: absolute; top: 378px; left: 148px; width: 44px; height: 2px; background: var(--navy);
  }
  .contacts { position: absolute; top: 411px; left: 43px; list-style: none; }
  .contact {
    display: flex; align-items: center; gap: 7px; height: 29px; margin-bottom: 11px;
    color: var(--ink); font-weight: 500; font-size: 17px; letter-spacing: 0.3px;
  }
  .contact-icon { width: 29px; height: 29px; flex: none; }
</style>
</head>
<body>
<main class="sheet">

  <section class="card card-front" aria-label="Card front">
    <div class="front-panels" role="img" aria-label="Angled side panels in teal"></div>
    <div class="brand-name">Marlow Hire</div>
    <div class="front-web">www.marlowhire.nz</div>
    <div class="bottom-bar"></div>
  </section>

  <section class="card card-back" aria-label="Card back">
    <div class="back-header" role="img" aria-label="Navy header with angled lower edge"></div>
    <div class="brand-name">Marlow Hire</div>

    <div class="person">
      <div class="person-name">HARRIET QUINN</div>
      <div class="person-role">Director | Senior Search Consultant</div>
    </div>

    <div class="hours">
      <div class="hours-days">Monday - Friday</div>
      <div class="hours-time">8:00am - 6:00pm NZST</div>
    </div>
    <div class="divider"></div>

    <ul class="contacts">
      <li class="contact">
        <svg class="contact-icon" viewBox="0 0 30 30" aria-hidden="true">
          <circle cx="15" cy="15" r="15" fill="var(--navy)"/>
          <path d="M10.5 8.5 l3 0 l1 3.5 l-2 1.3 a9 9 0 0 0 4.2 4.2 l1.3 -2 l3.5 1 l0 3 a1.5 1.5 0 0 1 -1.5 1.5 a12 12 0 0 1 -11 -11 a1.5 1.5 0 0 1 1.5 -1.5z" fill="var(--paper)"/>
        </svg>
        <span>+64 27 480 2291</span>
      </li>
      <li class="contact">
        <svg class="contact-icon" viewBox="0 0 30 30" aria-hidden="true">
          <circle cx="15" cy="15" r="15" fill="var(--navy)"/>
          <rect x="8" y="10" width="14" height="10" fill="none" stroke="var(--paper)" stroke-width="1.5"/>
          <path d="M8 10 l7 6 l7 -6 M8 20 l5 -5 M22 20 l-5 -5" fill="none" stroke="var(--paper)" stroke-width="1.3"/>
        </svg>
        <span>harriet@marlowhire.nz</span>
      </li>
      <li class="contact">
        <svg class="contact-icon" viewBox="0 0 30 30" aria-hidden="true">
          <circle cx="15" cy="15" r="15" fill="var(--navy)"/>
          <g fill="none" stroke="var(--paper)" stroke-width="1.3">
            <circle cx="15" cy="15" r="7"/>
            <ellipse cx="15" cy="15" rx="3" ry="7"/>
            <path d="M8 15 h14 M9 11.5 h12 M9 18.5 h12"/>
          </g>
        </svg>
        <span>www.marlowhire.nz</span>
      </li>
    </ul>
    <div class="bottom-bar"></div>
  </section>

</main>
</body>
</html>
```